Get referrals for Insurance customers and the domain name is tallyfinch.ca We are an insurance

We need a logo and a website for a referral site. Our advertising and promotion will send customers to this website where they will fill out a form giving their information as well as person they want to refer. The logo idea that I have is a gear with a dollar sign in it the number 2 and the letter U. Another words dollars to you. If this can be animated with sounds, that would be great. Once this form is filled in it goes to a referral software site such as Lantern Quay or Bonusvale where the data is saved for us to follow up. This is not a complicated site. It will reassure the people who will refer their friends, family members or other aquiatnces that we will provide great service to and best prices for home and business insurance. It will exclude auto insurance as not referral for a monitory reward(regulations). The reward will be $100 for business and house insurance and $25 condo or townhome insurance. It will imply that this $100 is limited time offer. The site should be set so that we could edit the website once the designer has given it to us. The people we expecting to be our referrers are real estate agents, notaries public, and our existing customers.
Updates

The designs are not what I was expecting. Is there any way I can communicate with the designer that I think made the best attempt at what I was expecting?

Target Market(s)

Our customers, realtors, notaries public and anyone who knows

Industry/Entity Type

Insurance Broker

Logo Text

Dollar sign, Gear, number 2 and U a funnel. Dollars to you . See what you can

Number of Pages Required

4 page

Font styles to use
Other font styles liked:
• Calibri

Colors
0455a3
ec1f27
ffffff

Requirements
Must have
• Fillable form on info about referer and the referred. This will data will be sent to the third party who will have our data for keeping track of the referrals and where Our referees can see how many people they have referred and who has been approved for payment. The third parties our such as Lantern Quay or Bonusvale.
Nice to have
• Animated logo with sound would be nice. This will be used on the website only. We use ashgrove insurance logo as seen on www,ashgroveinsurance.ca for all communications.
Should not have
• I have attached two files for reference only they do not have the exact text that I want to have on the website. I am working on that and it will always be changing to some extent. You can talk to me.

```html
<!DOCTYPE html>
<html lang="en">
<head>
<meta charset="utf-8">
<title>Tallyfinch – Get Referrals for Insurance</title>
<link href="https://fonts.googleapis.com/css2?family=Mulish:wght@400;600;700;800&family=Lato:wght@400;700&display=swap" rel="stylesheet">
<style>
:root{
  --blue:#0455a3;
  --blue-dark:#033f7a;
  --blue-mid:#1a6fc4;
  --red:#ec1f27;
  --white:#ffffff;
  --ink:#2b2f36;
  --muted:#6b7380;
  --line:#d9dee6;
  --pale:#f2f4f7;
}
*{box-sizing:border-box;margin:0;padding:0}
html,body{width:1200px;height:2500px;overflow:hidden}
body{font-family:"Lato",sans-serif;color:var(--ink);background:var(--white);position:relative}
h1,h2,h3,h4{font-family:"Mulish",sans-serif}

/* header */
.site-header{position:absolute;top:0;left:0;width:1200px;height:64px;background:var(--white);display:flex;align-items:center;justify-content:space-between;padding:0 40px 0 110px;z-index:3}
.brand{display:flex;align-items:center;gap:12px}
.brand-dot{width:40px;height:40px;border-radius:50%;background:var(--blue)}
.brand-name{font-family:"Mulish",sans-serif;font-weight:800;font-size:26px;color:var(--blue)}
.main-nav{display:flex;gap:30px;font-family:"Mulish",sans-serif;font-size:17px;font-weight:600}
.main-nav a{color:var(--ink);text-decoration:none}
.main-nav a.active{color:var(--red)}

/* hero */
.hero{position:absolute;top:64px;left:0;width:1200px;height:616px;background:linear-gradient(120deg,#c9cfd6 0%,#e6e1dc 40%,#b9a595 70%,#8d7766 100%)}
.hero-form{position:absolute;left:300px;top:168px;width:530px;height:300px;background:rgba(4,85,163,.88);padding:26px 30px;color:var(--white)}
.hero-form h1{font-size:24px;font-weight:700;margin-bottom:18px}
.form-row{display:flex;gap:10px;margin-bottom:10px}
.field{flex:1;height:28px;background:var(--white);border-radius:2px;font-size:12px;color:var(--muted);padding:6px 10px}
.checks{display:flex;align-items:center;gap:14px;font-size:11px;margin:6px 0 14px}
.checks span{display:flex;align-items:center;gap:5px}
.checks i{display:inline-block;width:11px;height:11px;background:var(--white)}
.btn-submit{display:inline-block;background:var(--red);color:var(--white);font-weight:700;font-size:13px;padding:8px 26px;border-radius:2px}

/* steps */
.steps{position:absolute;top:680px;left:0;width:1200px;height:290px}
.steps-title{text-align:center;color:var(--red);font-size:28px;font-weight:700;margin-top:50px}
.step-list{display:flex;justify-content:center;gap:50px;margin-top:34px}
.step{display:flex;gap:16px;width:270px}
.step-icon{flex:none;width:70px;height:70px;border-radius:50%;border:2px solid var(--line);display:flex;align-items:center;justify-content:center}
.step h3{color:var(--blue);font-size:19px;font-weight:700;margin-bottom:6px}
.step p{font-size:12px;color:var(--muted);line-height:1.5}
.chevron{position:absolute;left:0;top:880px;width:1200px;height:90px}

/* chances */
.chances-title{position:absolute;top:1000px;width:1200px;text-align:center;font-size:30px;font-weight:800;color:var(--ink)}
.cards{position:absolute;top:1060px;left:110px;width:980px;display:flex;gap:10px}
.card{flex:1;height:350px;color:var(--white);text-align:center}
.card-photo{height:140px}
.card-body{height:210px;padding:24px 30px}
.card-body h3{font-size:22px;font-weight:800;margin-bottom:12px}
.card-body p{font-size:13px;line-height:1.55}
.card.blue .card-body{background:var(--blue)}
.card.red .card-body{background:var(--red)}

/* help */
.help{position:absolute;top:1430px;left:0;width:1200px;height:400px;background:linear-gradient(90deg,#ffffff 45%,#eef1f4 100%)}
.help-photo{position:absolute;right:200px;top:30px;width:340px;height:370px;background:linear-gradient(180deg,#d5dae0,#4a5566 60%,#2d3440)}
.help-text{position:absolute;left:120px;top:90px;width:430px}
.help-text h2{font-size:34px;font-weight:800;margin-bottom:16px}
.help-text p{font-size:13px;line-height:1.6;color:var(--muted);margin-bottom:14px}
.help-list{list-style:none;font-size:13px;color:var(--ink)}
.help-list li{display:flex;align-items:center;gap:10px;margin-bottom:8px}
.tick{width:14px;height:14px;border-radius:50%;background:var(--red);flex:none}

/* testimonials */
.testimonials{position:absolute;top:1830px;left:0;width:1200px;height:510px;background:linear-gradient(180deg,var(--blue-mid),var(--blue))}
.testimonials h2{text-align:center;color:var(--white);font-size:28px;font-weight:700;margin-top:50px}
.t-line{width:60px;height:3px;background:var(--white);margin:12px auto 0}
.quotes{display:flex;justify-content:center;gap:60px;margin-top:46px}
.quote{width:350px;text-align:center}
.quote-box{background:var(--white);height:150px;padding:30px 34px;font-size:13px;color:var(--muted);line-height:1.6;font-style:italic}
.avatar{width:62px;height:62px;border-radius:50%;background:#c4b3a4;border:3px solid var(--white);margin:-30px auto 10px}
.quote cite{color:var(--white);font-size:13px;font-style:normal}

/* footer */
.site-footer{position:absolute;top:2340px;left:0;width:1200px;height:160px;background:var(--blue-dark);color:var(--white);padding:40px 140px}
.foot-nav{display:flex;gap:28px;font-family:"Mulish",sans-serif;font-weight:600;font-size:15px}
.social{position:absolute;right:140px;top:34px;display:flex;gap:10px}
.social span{width:30px;height:30px;border-radius:50%;border:2px solid var(--white)}
.copy{font-size:11px;opacity:.75;margin-top:22px}
</style>
</head>
<body>

<header class="site-header">
  <div class="brand"><span class="brand-dot"></span><span class="brand-name">Tallyfinch</span></div>
  <nav class="main-nav">
    <a class="active" href="#">Home</a><a href="#">About Us</a><a href="#">How it Works</a><a href="#">Prizes</a><a href="#">Testimonials</a><a href="#">Contact</a>
  </nav>
</header>

<section class="hero" role="img" aria-label="Photo of a smiling couple embracing">
  <form class="hero-form">
    <h1>Get Referrals for Insurance</h1>
    <div class="form-row"><div class="field">Name</div><div class="field">Address</div></div>
    <div class="form-row"><div class="field">City</div><div class="field">State</div><div class="field">Zip</div></div>
    <div class="form-row"><div class="field">Telephone</div><div class="field">Email</div></div>
    <div class="checks">
      <span>Best Time to Call</span><span><i></i>AM</span><span><i></i>PM</span><span><i></i>Referral Bonus</span><span><i></i>Home Insurance</span><span><i></i>Business Insurance</span>
    </div>
    <span class="btn-submit">SUBMIT</span>
  </form>
</section>

<section class="steps">
  <h2 class="steps-title">Refer a Friend, Reward Yourself</h2>
  <div class="step-list">
    <div class="step">
      <div class="step-icon"><svg width="30" height="34" viewBox="0 0 30 34" fill="none" stroke="#ec1f27" stroke-width="2.5"><rect x="3" y="2" width="24" height="30" rx="2"/><path d="M8 11h14M8 17h14M8 23h9"/></svg></div>
      <div><h3>1. Fill Our Form</h3><p>Share your details and the details of the friend you wish to refer today.</p></div>
    </div>
    <div class="step">
      <div class="step-icon"><svg width="34" height="34" viewBox="0 0 34 34" fill="none" stroke="#ec1f27" stroke-width="2.5"><path d="M4 4h13l13 13-13 13L4 17z"/><circle cx="11" cy="11" r="2.5"/></svg></div>
      <div><h3>2. Get an Offer</h3><p>We contact your friend with a quote for home or business insurance.</p></div>
    </div>
    <div class="step">
      <div class="step-icon"><svg width="32" height="34" viewBox="0 0 32 34" fill="none" stroke="#ec1f27" stroke-width="2.5"><path d="M8 3h16v10a8 8 0 0 1-16 0zM16 21v6M10 31h12M8 6H3v3a5 5 0 0 0 5 5M24 6h5v3a5 5 0 0 1-5 5"/></svg></div>
      <div><h3>3. Win Prizes</h3><p>Earn a cash reward for every referral who becomes an approved client.</p></div>
    </div>
  </div>
</section>

<svg class="chevron" viewBox="0 0 1200 90" preserveAspectRatio="none">
  <polygon points="0,0 1200,0 1200,10 600,80 0,10" fill="#f2f4f7"/>
  <polyline points="0,10 600,80 1200,10" fill="none" stroke="#ec1f27" stroke-width="4"/>
</svg>

<h2 class="chances-title">3 CHANCES FOR YOU TO WIN!</h2>
<div class="cards">
  <article class="card blue">
    <div class="card-photo" role="img" aria-label="Photo of a hand holding a gift card" style="background:linear-gradient(135deg,#9fc3e6,#3a7fc4)"></div>
    <div class="card-body"><h3>1ST CHANCE</h3><p>Every referral earns you $100 and 1 chance to win a gift card toward the grand prize draw.</p></div>
  </article>
  <article class="card blue">
    <div class="card-photo" role="img" aria-label="Photo of a fuel pump nozzle" style="background:linear-gradient(135deg,#d8dde3,#c2303a)"></div>
    <div class="card-body"><h3>2ND CHANCE</h3><p>Refer a friend and receive a fuel card. The first week each month adds extra draws.</p></div>
  </article>
  <article class="card red">
    <div class="card-photo" role="img" aria-label="Photo of colourful cupcakes" style="background:linear-gradient(135deg,#f3a7c6,#8fd0e8 50%,#f6d36b)"></div>
    <div class="card-body"><h3>GRAND PRIZE</h3><p>The grand prize draw rewards one lucky referrer with a weekend getaway for two.</p></div>
  </article>
</div>

<section class="help">
  <div class="help-text">
    <h2>WE CAN HELP!</h2>
    <p>Ashgrove Insurance, established since 1966, is an independent full service insurance agency located in Surrey. Our office is open late 7 days a week to provide our clients with great customer experience by:</p>
    <ul class="help-list">
      <li><span class="tick"></span>Assuring proper coverage</li>
      <li><span class="tick"></span>Providing excellent customer service</li>
      <li><span class="tick"></span>Obtaining lowest premium</li>
      <li><span class="tick"></span>Offering free mobile service</li>
    </ul>
  </div>
  <div class="help-photo" role="img" aria-label="Photo of a smiling businessman in a suit"></div>
</section>

<section class="testimonials">
  <h2>TESTIMONIALS</h2>
  <div class="t-line"></div>
  <div class="quotes">
    <figure class="quote">
      <blockquote class="quote-box">Working with this team was easy and friendly. They found me a better rate and great coverage fast.</blockquote>
      <div class="avatar" role="img" aria-label="Portrait of the reviewer"></div>
      <cite>By Author Name, City Location</cite>
    </figure>
    <figure class="quote">
      <blockquote class="quote-box">Working with this team was easy and friendly. They found me a better rate and great coverage fast.</blockquote>
      <div class="avatar" role="img" aria-label="Portrait of the reviewer"></div>
      <cite>By Author Name, City Location</cite>
    </figure>
  </div>
</section>

<footer class="site-footer">
  <nav class="foot-nav"><span>Home</span><span>About Us</span><span>How it Works</span><span>Prizes</span><span>Testimonials</span><span>Contact</span></nav>
  <div class="social"><span></span><span></span><span></span><span></span></div>
  <p class="copy">© 2024 Tallyfinch. All rights reserved. Terms of Use</p>
</footer>

</body>
</html>
```